Need a solid log.
My company Sales: OrbiCast, Halcyon Beam, Vorlan Internet
Design and installation of WI_FI systems.
Fulfillment company for installations in the Electronics industry

Industry/Entity Type

Electronics

Contact Information for Business Card

Peter R. Hollowell
President
Phone: 479.555.0182 Cell: 479.5550947 prhollowell@brightharbornet.biz
Bright Harbor Networks
Maplecrest, TN. 38201

```html
<!DOCTYPE html>
<html lang="en">
<head>
<meta charset="utf-8">
<title>Bright Harbor Networks – Business Card</title>
<link rel="stylesheet" href="https://fonts.googleapis.com/css2?family=Bebas+Neue&display=swap">
<style>
  :root {
    --card-bg: #ffffff;
    --brand-red: #ee0000;
    --ink: #111111;
    --muted: #555555;
    --icon: #ffffff;
  }
  * { margin: 0; padding: 0; box-sizing: border-box; }
  html, body { width: 1200px; height: 703px; overflow: hidden; background: var(--card-bg); }
  .card {
    position: relative;
    width: 1200px;
    height: 703px;
    overflow: hidden;
    background: var(--card-bg);
    font-family: "Bebas Neue", "Arial Narrow", sans-serif;
    color: var(--ink);
  }
  .brand-shapes { position: absolute; inset: 0; width: 1200px; height: 703px; }
  .contact { position: absolute; left: 66px; top: 66px; line-height: 1; }
  .contact__name { font-size: 64px; font-weight: 400; letter-spacing: 1px; }
  .contact__title { font-size: 32px; color: var(--muted); margin-top: 2px; }
  .contact__line { font-size: 35px; margin-top: 8px; }
  .services { position: absolute; left: 66px; top: 356px; font-size: 28px; line-height: 1; letter-spacing: 0.5px; }
  .services p { margin-bottom: 14px; color: var(--muted); }
  .services .services__tight { margin-bottom: 2px; }
  .services strong { font-weight: 400; color: var(--ink); }
  .footer {
    position: absolute; left: 50px; top: 610px;
    display: flex; align-items: center;
    font-size: 31px; color: var(--brand-red); letter-spacing: 0.5px;
  }
  .footer__icon { width: 40px; height: 40px; margin-right: 6px; }
  .footer__company { margin-left: 56px; }
</style>
</head>
<body>
<div class="card">
  <svg class="brand-shapes" viewBox="0 0 1200 703" aria-hidden="true">
    <g fill="var(--brand-red)">
      <circle cx="1062" cy="88" r="222"/>
      <circle cx="1128" cy="365" r="190"/>
      <circle cx="1138" cy="588" r="200"/>
    </g>
    <g class="icon-wifi" fill="none" stroke="var(--icon)" stroke-width="11" stroke-linecap="round">
      <path d="M1025 128 a68 68 0 0 1 96 0"/>
      <path d="M1040 145 a46 46 0 0 1 66 0"/>
      <path d="M1055 162 a24 24 0 0 1 36 0"/>
      <circle cx="1073" cy="180" r="6" fill="var(--icon)" stroke="none"/>
    </g>
    <g class="icon-dish" fill="var(--icon)">
      <path d="M1030 320 l58 58 a41 41 0 0 1 -58 -58 z" transform="rotate(10 1060 350)"/>
      <rect x="1052" y="378" width="10" height="18"/>
      <rect x="1036" y="394" width="42" height="8" rx="2"/>
      <line x1="1060" y1="350" x2="1088" y2="322" stroke="var(--icon)" stroke-width="5"/>
      <circle cx="1090" cy="320" r="6"/>
      <g fill="none" stroke="var(--icon)" stroke-width="5" stroke-linecap="round">
        <path d="M1095 303 a18 18 0 0 1 14 14"/>
        <path d="M1097 290 a30 30 0 0 1 25 25"/>
      </g>
    </g>
    <g class="icon-tv" fill="none" stroke="var(--icon)" stroke-width="8" stroke-linejoin="round" stroke-linecap="round">
      <rect x="1034" y="534" width="78" height="58" rx="4"/>
      <line x1="1058" y1="508" x2="1073" y2="532"/>
      <line x1="1090" y1="508" x2="1073" y2="532"/>
      <line x1="1050" y1="596" x2="1050" y2="602"/>
      <line x1="1096" y1="596" x2="1096" y2="602"/>
    </g>
  </svg>

  <section class="contact">
    <h1 class="contact__name">Peter R. Hollowell</h1>
    <p class="contact__title">President</p>
    <p class="contact__line">479.5550947</p>
    <p class="contact__line">prhollowell@brightharbornet.biz</p>
  </section>

  <section class="services">
    <p>Sales &amp; services include <strong>OrbiCast, Halcyon Beam &amp; Vorlan Internet</strong></p>
    <p>Specialized in <strong>Wi_Fi systems design &amp; installation</strong></p>
    <p class="services__tight">Well known fulfillment company for</p>
    <p>installations in the electronics industry</p>
  </section>

  <footer class="footer">
    <svg class="footer__icon" viewBox="0 0 40 40" aria-hidden="true">
      <circle cx="20" cy="20" r="19" fill="var(--brand-red)"/>
      <path d="M13 10 l5 0 l2 6 l-3 2 a14 14 0 0 0 6 6 l2 -3 l6 2 l0 5 a3 3 0 0 1 -3 3 a20 20 0 0 1 -18 -18 a3 3 0 0 1 3 -3 z" fill="var(--icon)"/>
    </svg>
    <span class="footer__phone">479.555.0182</span>
    <span class="footer__company">Bright Harbor Networks Maplecrest, TN. 38201</span>
  </footer>
</div>
</body>
</html>
```